Wordpress Design for Financial Trading Software

Our Software QuantoMoss allows clients to program their trading strategy and use it to trade automatically on stock markets. For further details please visit our preliminary / draft web page: http://www.quantomoss.example/wordpress.
We would like the Web Page to represent the following values:
- Innovative
- High Tech
- High Quality
- Professional
- Sophisticated
- State-of-the-art
- Modern
- Versatile
We need a Design based on a PSD file for the Main Page containing the following:
Header:
- Logo + optional Image / Graphic / Slogan / Quote
- Menu Bar with drop-down for Sub-Menus
- Search Box
Full Width Featured Content Area
- Main Description of the Product (with read-more Link + optional Image / Graphic)
Smaller Featured Content Areas:
- Product Features (with read-more Link + optional Icon)
- Documentation and Demo (with read-more Link + optional Icon)
- Professional Services (with read-more Link + optional Icon)
- Training (with read-more Link + optional Icon)
Latest News:
- 3-5 latest News + option Image / Grafic
Testimonial:
- 1 Customer Testimonial with Photo
Footer:
- Copyright and "all rights reserved" Notice
- Privacy Policy
- Contact Info: Address, Phone Number and Email
- Link to Site-Map
- Social Media Connectors (Friendwall, LinkedIn, RSS Feed & Email)
Guidelines for Style/Theme:
- Well structured, Lean, Easy-to-use Page
- Use of existing Logo
- Sans-Serif Fonts
- Colors matching our Logo (not too many Colors)
- Main Focus: Desktop-Computers.
- However: Page should be readable on mobile Devices also
- Please show one element of the navigation bar in selected state with drop-down
- After the contest we will work with the Designer on the other Pages
- We will need a PSD File, so that we can organize the actual coding of the Wordpress Page / Theme
- If images / photos are used, they have to be royalty-free.
Example Pages that we like:
http://www.bervinkolo.example/
http://www.qtz.example/
http://www.layrumbo.example/
http://www.swapholm.example/
http://www.nimbrofarm.example/
http://www.corvalex.example/
http://www.plg-gewerbehafen.example/
https://www.o-tilvan.example/
http://www.pelmquarry.example/
https://sketchbarn.example/web-design/contests/bright-water-ventures-exchange-portal-website-design-573821/entries/48213967
https://sketchbarn.example/web-design/contests/website-design-wanted-hollarby-group-62718/entries/7304521
http://files.drawmarket.example/design_img/481726/37452/37452_9027315_481726_image.jpg
WordPress Plugins currently in use:
- Quick Sealed Inquiry Panel
- Glowpane Album
- ChartLeaf Simple Terrain Plots
Project Deadline Extended
Reason: A few Designers let us know, that they need more time to work on their Designs. We are in no rush and would like to see as many good Designs as possible!
Target Market(s)
Investment Banks and Hedge Funds
Industry/Entity Type
Trade

```html
<!DOCTYPE html>
<html lang="en">
<head>
<meta charset="utf-8">
<title>QuantoMoss — Algorithmic Trading Software</title>
<link href="https://fonts.googleapis.com/css2?family=Arimo:wght@400;700&family=Roboto+Condensed:wght@300;400;700&display=swap" rel="stylesheet">
<style>
:root{
  --gold:#d6bb6c;
  --gold-deep:#b3955a;
  --gold-soft:#e9dca6;
  --ink:#3b4248;
  --ink-soft:#5c656c;
  --muted:#9aa0a6;
  --slate:#6e8494;
  --slate-dark:#4d5a64;
  --footer:#31353a;
  --footer-line:#45494f;
  --footer-text:#c9ccd0;
  --bar:#111214;
  --white:#ffffff;
  --rule:#e1e3e5;
}
*{margin:0;padding:0;box-sizing:border-box}
html,body{width:1200px;height:2606px;overflow:hidden}
body{position:relative;background:var(--white);font-family:"Arimo",Arial,sans-serif;color:var(--ink)}
.abs{position:absolute}

/* header */
.site-header{left:0;top:0;width:1200px;height:150px;background:var(--white)}
.search-box{left:961px;top:11px;width:212px;height:40px;background:linear-gradient(#f6f4ec,#e6e2d2);border-radius:3px;font-size:15px;color:#555;padding:11px 0 0 16px}
.search-box svg{position:absolute;right:10px;top:8px}
.brand{left:66px;top:62px;display:flex;align-items:center;gap:12px;font-family:"Roboto Condensed",sans-serif;font-weight:700;font-size:40px;color:var(--ink)}
.brand .mark{width:28px;height:28px;background:var(--gold)}
.main-nav{top:94px;left:0;width:1200px;height:22px}
.main-nav a{position:absolute;font-family:"Roboto Condensed",sans-serif;font-size:14px;color:var(--ink);text-decoration:none;transform:translateX(-50%);top:2px}
.main-nav .current{background:linear-gradient(#efe1a8,#d8c17a);padding:10px 14px;top:-12px;border:1px solid #c9b168}

.dropdown{left:819px;top:135px;width:179px;height:175px;background:var(--slate-dark);box-shadow:0 3px 6px rgba(0,0,0,.35);padding:6px 4px}
.dropdown li{list-style:none;height:37px;margin-bottom:4px;background:linear-gradient(#5f6f7b,#48545d);color:var(--gold-soft);font-size:14px;padding:11px 0 0 26px;font-family:"Roboto Condensed",sans-serif}
.dropdown li.active{background:linear-gradient(#f1e3ad,#dcc57f);color:var(--ink)}

/* hero */
.hero{left:0;top:150px;width:1200px;height:465px;background:radial-gradient(ellipse at 45% 40%,#efe2b0 0%,#cdb473 45%,#a58c52 100%)}
.hero-title{left:51px;top:233px;font-family:"Roboto Condensed",sans-serif;font-weight:700;font-size:23px;color:#3a3a36}
.hero-text{left:51px;top:283px;width:404px;font-size:13px;line-height:16.4px;color:#2e2d28}
.btn{display:block;text-align:center;font-family:"Roboto Condensed",sans-serif;font-size:14px;border-radius:4px;text-decoration:none}
.btn-slate{background:linear-gradient(#7c93a3,#5b6f7d);color:var(--white);border:1px solid #4a5965}
.btn-gold{background:linear-gradient(#f2e3a4,#cdb064);color:#3a3a36;border:1px solid #a68d4b}
.hero-read{left:49px;top:460px;width:111px;height:40px;line-height:38px}
.hero-demo{left:173px;top:460px;width:110px;height:40px;line-height:38px}
.hero-art{left:609px;top:261px;width:553px;height:304px;border-radius:6px;background:linear-gradient(100deg,rgba(40,40,50,.25),rgba(200,60,60,.25) 40%,rgba(70,120,200,.3) 70%,rgba(40,40,50,.25))}
.slider-dots{left:527px;top:587px;display:flex;gap:6px}
.slider-dots span{width:13px;height:13px;border-radius:50%;background:#d9cfae;border:1px solid #9d8c5d}
.slider-dots span.on{background:var(--slate-dark)}

/* intro */
.intro{left:50px;top:668px;width:1100px;text-align:center;font-family:"Roboto Condensed",sans-serif;font-weight:300;font-size:27px;line-height:33px;color:var(--ink-soft)}
.intro strong{color:var(--gold);font-weight:400}

/* features */
.feature{top:820px;width:260px;text-align:center}
.feature .icon{margin:0 auto;width:74px;height:74px;border-radius:50%;display:flex;align-items:center;justify-content:center;box-shadow:0 2px 4px rgba(0,0,0,.25)}
.feature h3{margin-top:23px;height:44px;font-family:"Roboto Condensed",sans-serif;font-weight:700;font-size:16px;line-height:18px;color:var(--ink)}
.feature p{margin:4px auto 0;width:205px;font-size:12.4px;line-height:19.5px;color:#444;text-align:justify;height:78px}
.feature .btn{margin:17px auto 0;width:78px;height:24px;line-height:22px;font-size:11px;border-radius:3px}

.rule{height:1px;background:var(--rule)}

/* company + news */
.section-title{font-family:"Roboto Condensed",sans-serif;font-weight:700;font-size:19px;color:var(--ink)}
.tabs{left:27px;top:1262px;display:flex}
.tabs span{font-family:"Roboto Condensed",sans-serif;font-size:13px;color:var(--gold);padding:8px 14px;height:32px}
.tabs span.on{color:var(--ink);border:1px solid var(--rule);border-bottom-color:var(--white);background:var(--white);position:relative;z-index:1}
.tab-panel{left:27px;top:1293px;width:631px;height:292px;border:1px solid var(--rule);border-radius:0 4px 4px 4px;box-shadow:0 1px 3px rgba(0,0,0,.08)}
.clock-art{left:40px;top:1355px;width:133px;height:117px;border-radius:50%;background:radial-gradient(circle,#fff 40%,#f3a53a 42%,#d9701c 100%)}
.tab-text{left:213px;top:1341px;width:414px;font-size:12.6px;line-height:19px;color:#444;text-align:justify}
.tab-demo{left:210px;top:1532px;width:107px;height:31px;line-height:29px;font-size:15px;font-weight:700}

.news-item{left:786px;width:387px;height:90px}
.news-item .thumb{position:absolute;left:0;top:0;width:73px;height:60px;background:linear-gradient(135deg,#f2f2f2,#8b8f93 60%,#3c3f42)}
.news-item p{position:absolute;left:100px;top:-3px;width:287px;font-size:12.6px;line-height:19px;color:#a7abaf;text-align:justify;height:57px;overflow:hidden}
.news-item time{position:absolute;right:0;top:64px;font-size:13px;font-style:italic;color:var(--ink)}
.see-more{left:1091px;top:1561px;width:82px;height:24px;line-height:24px;font-size:11px;border-radius:3px;background:linear-gradient(#ecdba0,#d3ba72);color:var(--white)}

/* testimonials */
.testi-head{left:500px;top:1688px;width:200px;background:var(--white);text-align:center}
.testi-sub{left:300px;top:1722px;width:600px;text-align:center;font-size:14px;color:var(--gold)}
.testimonial{top:1806px;width:240px;text-align:center}
.testimonial .photo{margin:0 auto;width:116px;height:116px;border-radius:50%;background:radial-gradient(circle at 50% 40%,#e6c3a6 0%,#b78f73 45%,#d8dde2 70%);border:3px solid #fff;box-shadow:0 1px 4px rgba(0,0,0,.3)}
.testimonial h4{margin-top:14px;font-size:10.5px;font-weight:700;color:var(--ink)}
.testimonial p{margin:12px auto 0;width:210px;font-size:12.6px;line-height:20px;color:#444;text-align:justify}
.arrow{top:1918px}

/* footer */
.site-footer{left:0;top:2203px;width:1200px;height:361px;background:var(--footer)}
.footer-col{top:2226px}
.footer-col h5{font-family:"Roboto Condensed",sans-serif;font-weight:700;font-size:15px;color:var(--gold)}
.footer-col ul{margin-top:52px;list-style:none}
.footer-col li{font-size:11.5px;line-height:20.9px;color:var(--footer-text);text-transform:uppercase}
.footer-divider{top:2226px;width:1px;height:322px;background:var(--footer-line)}
.social{left:655px;top:2305px}
.social li{list-style:none;display:flex;align-items:center;gap:14px;height:39px;font-family:"Roboto Condensed",sans-serif;font-weight:700;font-size:15px;color:var(--footer-text)}
.social li span{width:29px;height:29px;border-radius:50%;background:#7d848b}
.subscribe{left:655px;top:2464px;width:215px;height:36px;background:var(--white);border-radius:3px;font-size:11px;color:#888;padding:12px 0 0 14px}
.subscribe b{position:absolute;right:8px;top:6px;width:50px;height:24px;line-height:24px;text-align:center;background:var(--footer);color:var(--white);font-weight:400;border-radius:2px}
.footer-brand{left:959px;top:2290px;display:flex;align-items:center;gap:10px;font-family:"Roboto Condensed",sans-serif;font-weight:700;font-size:36px;color:#8e949a}
.footer-brand .mark{width:24px;height:24px;background:var(--gold)}
.address{left:959px;top:2412px;font-size:12.5px;line-height:24.5px;color:var(--footer-text);font-style:normal}
.copyright{left:0;top:2564px;width:1200px;height:42px;background:var(--bar);color:var(--white);font-size:11.5px;text-align:center;line-height:42px;text-transform:uppercase}
</style>
</head>
<body>

<header class="site-header abs">
  <div class="search-box abs">Searh Keywords
    <svg width="26" height="24" viewBox="0 0 26 24"><circle cx="10" cy="10" r="7" fill="none" stroke="#333" stroke-width="3"/><line x1="15" y1="15" x2="23" y2="22" stroke="#333" stroke-width="4" stroke-linecap="round"/></svg>
  </div>
  <div class="brand abs"><span class="mark"></span>QuantoMoss</div>
  <nav class="main-nav abs">
    <a style="left:693px">HOME</a>
    <a style="left:773px">ABOUT US</a>
    <a class="current" style="left:865px">SERVICES</a>
    <a style="left:959px">PORTFOLIO</a>
    <a style="left:1041px">BLOG</a>
    <a style="left:1127px">CONTACT US</a>
  </nav>
</header>

<section class="hero abs" aria-label="Featured product"></section>
<h1 class="hero-title abs">QUANTOMOSS SOFTWARE</h1>
<p class="hero-text abs">Lorem Ipsum is simply dummy text of the printing and typesetting industry. Lorem Ipsum has been the industry's standard dummy text ever since the 1500s, when an unknown printer took a galley of type and scrambled it to make a type specimen book. It has survived not only five centuries, but also the leap into electronic typesetting, remaining essentially unchanged. It was popularised in the 1960s with the release of Vellumtype sheets containing Lorem</p>
<a class="btn btn-slate hero-read abs">READ MORE</a>
<a class="btn btn-gold hero-demo abs">GET DEMO</a>
<div class="hero-art abs" role="img" aria-label="Business people in silhouette beside rising red and blue growth arrows"></div>
<div class="slider-dots abs"><span></span><span></span><span></span><span class="on"></span></div>

<ul class="dropdown abs">
  <li>Services</li>
  <li class="active">Services</li>
  <li>Services</li>
  <li>Services</li>
</ul>

<p class="intro abs">Hello ! We are &nbsp;<strong>QUANTOMOSS</strong>&nbsp; This is a &nbsp;BUSSINESS IT development Software &nbsp;which &nbsp;specializing in Forex. Bussiness Marketing &nbsp;and Best Trade Marketing Bussiness development Software</p>

<div class="feature abs" style="left:0">
  <div class="icon" style="background:radial-gradient(#f5dc86,#c9a64a)"><svg width="30" height="34" viewBox="0 0 30 34"><circle cx="15" cy="13" r="10" fill="#5b4a1c"/><rect x="10" y="23" width="10" height="7" rx="2" fill="#5b4a1c"/></svg></div>
  <h3>PRODUCT FEATURES</h3>
  <p>Lorem Ipsum is simply dummy text of the printing and typesetting industry. Lorem Ipsum has been the industry's standard dummy text</p>
  <a class="btn btn-slate">READ MORE</a>
</div>
<div class="feature abs" style="left:315px">
  <div class="icon" style="background:radial-gradient(#8fa2b0,#56697a)"><svg width="34" height="28" viewBox="0 0 34 28"><path d="M2 4h11l3 3h16v19H2z" fill="#eef1f3"/></svg></div>
  <h3>DOCUMENTAION<br>AND DEMO</h3>
  <p>Lorem Ipsum is simply dummy text of the printing and typesetting industry. Lorem Ipsum has been the industry's standard dummy text</p>
  <a class="btn btn-slate">READ MORE</a>
</div>
<div class="feature abs" style="left:629px">
  <div class="icon" style="background:radial-gradient(#8fa2b0,#56697a)"><svg width="34" height="28" viewBox="0 0 34 28"><rect x="2" y="7" width="30" height="19" rx="2" fill="#eef1f3"/><rect x="12" y="2" width="10" height="6" fill="none" stroke="#eef1f3" stroke-width="2"/></svg></div>
  <h3>PROFESSIONAL<br>SERVICES</h3>
  <p>Lorem Ipsum is simply dummy text of the printing and typesetting industry. Lorem Ipsum has been the industry's standard dummy text</p>
  <a class="btn btn-slate">READ MORE</a>
</div>
<div class="feature abs" style="left:942px">
  <div class="icon" style="background:radial-gradient(#8fa2b0,#56697a)"><svg width="26" height="34" viewBox="0 0 26 34"><path d="M13 2c6 6 7 14 5 22H8C6 16 7 8 13 2z" fill="#eef1f3"/><path d="M8 20l-5 8h6zM18 20l5 8h-6z" fill="#eef1f3"/></svg></div>
  <h3>TRAINING</h3>
  <p>Lorem Ipsum is simply dummy text of the printing and typesetting industry. Lorem Ipsum has been the industry's standard dummy text</p>
  <a class="btn btn-slate">READ MORE</a>
</div>

<div class="rule abs" style="left:0;top:1145px;width:1200px"></div>

<h2 class="section-title abs" style="left:27px;top:1197px">SOMETHINGS ABOUT OUR COMAPNY</h2>
<div class="tabs abs"><span class="on">PRODUCT</span><span>PRODUCT FEATURES</span><span>ABOUT US</span></div>
<div class="tab-panel abs"></div>
<div class="clock-art abs" role="img" aria-label="Orange alarm clock with a padlock"></div>
<p class="tab-text abs">Lorem Ipsum is simply dummy text of the printing and typesetting industry. Lorem Ipsum has been the industry's standard dummy text ever since the 1500s, when an unknown printer took a galley of type and scrambled it to make a type specimen book. It has survived not only five centuries, but also the leap into electronic typesetting, remaining essentially unchanged. It was popularised in the 1960s with the release of Vellumtype sheets containing Lorem Ipsum passages, and more recently with desktop publishing software like Pressmill Layout including</p>
<a class="btn btn-slate tab-demo abs">GET DEMO</a>

<h2 class="section-title abs" style="left:786px;top:1197px">LATEST NEWS</h2>
<article class="news-item abs" style="top:1255px">
  <div class="thumb" role="img" aria-label="Hand pointing at a touch screen"></div>
  <p>Lorem Ipsum is simply dummy text of the printing and typesetting industry. Lorem Ipsum has been the industry's standard dummy text ever since the</p>
  <time>May 5-2013</time>
</article>
<article class="news-item abs" style="top:1366px">
  <div class="thumb" role="img" aria-label="Hand pointing at a touch screen"></div>
  <p>Lorem Ipsum is simply dummy text of the printing and typesetting industry. Lorem Ipsum has been the industry's standard dummy text ever since the</p>
  <time>May 5-2013</time>
</article>
<article class="news-item abs" style="top:1466px">
  <div class="thumb" role="img" aria-label="Hand pointing at a touch screen"></div>
  <p>Lorem Ipsum is simply dummy text of the printing and typesetting industry. Lorem Ipsum has been the industry's standard dummy text ever since the</p>
  <time>May 5-2013</time>
</article>
<a class="btn see-more abs">SEE MORE</a>

<div class="rule abs" style="left:0;top:1700px;width:1200px"></div>
<h2 class="section-title testi-head abs">TESTIMONIALS</h2>
<p class="testi-sub abs">You can Judge us by the testimonials of our clients</p>

<div class="testimonial abs" style="left:179px">
  <div class="photo" role="img" aria-label="Portrait photo of a client"></div>
  <h4>Mr. Paul ( CEO of Company Name)</h4>
  <p>Lorem Ipsum is simply dummy text of the printing and typesetting industry. Lorem Ipsum has been the industry's standard dummy text ever</p>
</div>
<div class="testimonial abs" style="left:480px">
  <div class="photo" role="img" aria-label="Portrait photo of a client"></div>
  <h4>Mrs. Marya ( CEO of Company Name)</h4>
  <p>Lorem Ipsum is simply dummy text of the printing and typesetting industry. Lorem Ipsum has been the industry's standard dummy text ever</p>
</div>
<div class="testimonial abs" style="left:783px">
  <div class="photo" role="img" aria-label="Portrait photo of a client"></div>
  <h4>Mr. Paul ( CEO of Company Name)</h4>
  <p>Lorem Ipsum is simply dummy text of the printing and typesetting industry. Lorem Ipsum has been the industry's standard dummy text ever</p>
</div>
<svg class="arrow abs" style="left:38px" width="24" height="50" viewBox="0 0 24 50"><path d="M20 2L4 25l16 23" fill="none" stroke="#c8cbce" stroke-width="5"/></svg>
<svg class="arrow abs" style="left:1138px" width="24" height="50" viewBox="0 0 24 50"><path d="M4 2l16 23L4 48" fill="none" stroke="#c8cbce" stroke-width="5"/></svg>

<footer class="site-footer abs"></footer>
<div class="footer-divider abs" style="left:294px"></div>
<div class="footer-divider abs" style="left:611px"></div>
<div class="footer-divider abs" style="left:917px"></div>

<div class="footer-col abs" style="left:27px">
  <h5>QUICK LINKS</h5>
  <ul><li>Home</li><li>About us</li><li>Our Services</li><li>Blog</li><li>Video</li><li>News</li><li>Privacy Policy</li><li>Sitemap</li><li>Contact Us</li></ul>
</div>
<div class="footer-col abs" style="left:339px">
  <h5>SERVICES</h5>
  <ul><li>Services</li><li>Services</li><li>Services</li><li>Services</li><li>Services</li><li>Services</li><li>Services</li></ul>
</div>
<div class="footer-col abs" style="left:655px"><h5>GET IN TOUCH WITH US</h5></div>
<ul class="social abs">
  <li><span></span>Friendwall</li>
  <li><span></span>Circlecast</li>
  <li><span></span>Chirpline</li>
</ul>
<div class="subscribe abs">ENTER YOUR EMAIL<b>GO</b></div>

<div class="footer-col abs" style="left:959px"><h5>CONTACT US</h5></div>
<div class="footer-brand abs"><span class="mark"></span>QuantoMoss</div>
<address class="address abs">4120 Calloway Ridge<br>Denbrook MI 48990<br>Call us : 555-014-288<br>Toll Free : 855-QUANTO MOSS</address>

<div class="copyright abs">All copyright are reserved by QuantoMoss</div>

</body>
</html>
```